Illustrationen für ein Balance Boards
Zielgruppe
Meine Firma verkauft Balance Boards und Skateboards.
Ich habe meine Balance Board Designs von meinen anderen 2 Produkten verlinkt.
Ich verlinke hier einmal meine Produkte und dabei wird die Zielgruppe deutlich klarer anhand der Bewertungen usw.
1. https://www.kaufwelt-beispiel.de/dp/Q71TRM5XWA?ref=myi_title_dp
2. https://www.kaufwelt-beispiel.de/dp/Q71JNH4ZRE?ref=myi_title_dp
Es soll dabei ein neues Design erstellt werden für das Board, welches auf dem Karton liegt.
Es wäre dabei gut, wenn das Bild 3D gerendert wird oder einfach das Bild von der Konkurrenz verwendet wird.
Das ist nicht das gleiche Board, aber relativ ähnlich.
Aufgabenstellung
Wichtig beim Design ist das es leicht sein soll neue Varianten zu erstellen indem man einfach die Farbe verändert. Das sieht man anhand von meinen anderen Produkten.
Das Logo war zudem immer sehr dominant auf meinen Produkten, aber ich bin bereit neue Optionen zusehen.

```html
<!DOCTYPE html>
<html lang="de">
<head>
<meta charset="utf-8">
<title>KippWerk 180 – Banner</title>
<link rel="stylesheet" href="https://fonts.googleapis.com/css2?family=Russo+One&display=swap">
<style>
  :root {
    --brand-red: #8f1d1e;
    --accent-gold: #cfb06d;
    --accent-grey: #585858;
    --ink-white: #ffffff;
    --dot-tint: #c98b80;
  }
  html, body {
    margin: 0;
    padding: 0;
    overflow: hidden;
    background: var(--brand-red);
  }
  .banner {
    position: relative;
    width: 1200px;
    height: 284px;
    overflow: hidden;
    background: var(--brand-red);
  }
  .banner__art {
    position: absolute;
    inset: 0;
    width: 1200px;
    height: 284px;
  }
  .brand-name {
    font-family: "Russo One", sans-serif;
    font-size: 118px;
    fill: var(--ink-white);
  }
</style>
</head>
<body>
  <main class="banner">
    <svg class="banner__art" viewBox="0 0 1200 284" xmlns="http://www.w3.org/2000/svg">
      <defs>
        <linearGradient id="hatch-fade" x1="0" y1="0" x2="1" y2="0">
          <stop offset="0" stop-color="#ffffff" stop-opacity="0.45"/>
          <stop offset="1" stop-color="#ffffff" stop-opacity="0"/>
        </linearGradient>
        <radialGradient id="wave-glow" cx="0.5" cy="0.5" r="0.5">
          <stop offset="0" stop-color="#ffffff" stop-opacity="0.22"/>
          <stop offset="1" stop-color="#ffffff" stop-opacity="0"/>
        </radialGradient>
      </defs>

      <ellipse class="wave-mesh" role="img" aria-label="Feines weißes Linienwellen-Muster"
               cx="700" cy="120" rx="360" ry="170" fill="url(#wave-glow)"/>

      <rect class="hatch-band" role="img" aria-label="Weiße Schraffurlinien"
            x="0" y="0" width="305" height="42" fill="url(#hatch-fade)"/>

      <circle class="disc disc--gold" cx="309" cy="146" r="164" fill="var(--accent-gold)"/>

      <circle class="dot-field" role="img" aria-label="Weißes Punktraster im Kreis"
              cx="130" cy="192" r="92" fill="var(--dot-tint)" opacity="0.75"/>
      <circle class="dot-field" role="img" aria-label="Weißes Punktraster im Halbkreis"
              cx="591" cy="290" r="83" fill="var(--dot-tint)" opacity="0.75"/>

      <circle class="disc disc--grey" cx="746" cy="316" r="104" fill="var(--accent-grey)"/>

      <text class="brand-name" x="597" y="174" text-anchor="middle"
            textLength="705" lengthAdjust="spacingAndGlyphs">KippWerk 180</text>
    </svg>
  </main>
</body>
</html>
```